Web based Nutrition counceling needs a brochure

We need a two sided brochure design for our company "Quorvane Health". We provide nutrition counceling for consumers who wants to lose weight, diabetes care, high cholestrol or switching to healthier lifestyle. The brochure should compliment the colors in our logo.
Updates

The message should be we provide, 1) PRivate one-on-One Nutrition counceling in the comfort of your home 2) Counceling provided by Registered dietitians. 3) Nutrition counceling through HIPAA compliant video conferencing 4) Nutrition program and results overseen by primary care physicians 5) Nutrition therapy to better handle diabetes, high Cholesterol, Triglycerides & Blood Pressure 6) Pre-Post Natal Nutrition & Pediatric Nutrition 7) Overcome barriers such as emotional or disordered eating. 8) Provide meal-plans and help in creating grocery shopping list.

Industry/Entity Type

Nutrition

```html
<!DOCTYPE html>
<html lang="en">
<head>
<meta charset="UTF-8">
<title>Quorvane Health – Nutrition Counseling Brochure</title>
<link href="https://fonts.googleapis.com/css2?family=Ubuntu:wght@400;500;700&display=swap" rel="stylesheet">
<style>
  :root {
    --backdrop: #dcdcdc;
    --paper: #ffffff;
    --orange: #f08a24;
    --orange-deep: #e9791c;
    --orange-light: #f39a3c;
    --band: rgba(150, 80, 20, 0.35);
    --ink-grey: #5a5a5a;
    --ink-orange: #ef7d16;
    --white: #ffffff;
  }
  * { box-sizing: border-box; margin: 0; padding: 0; }
  html, body {
    width: 1200px; height: 1000px; overflow: hidden;
    background: var(--backdrop);
    font-family: "Ubuntu", sans-serif;
  }
  .spread { position: relative; width: 1200px; height: 1000px; }
  .sheet {
    position: absolute; top: 100px;
    width: 540px; height: 800px;
    background: var(--paper);
    overflow: hidden;
    box-shadow: 0 6px 18px rgba(0,0,0,0.18);
  }
  .sheet--front { left: 40px; }
  .sheet--back  { left: 620px; }

  /* brand header */
  .brand { position: absolute; right: 32px; text-align: right; }
  .brand__name {
    display: flex; align-items: center; justify-content: flex-end; gap: 12px;
    font-size: 34px; font-weight: 500; color: var(--ink-grey);
  }
  .brand__dot {
    width: 22px; height: 22px; border-radius: 50%;
    background: var(--ink-orange);
  }
  .brand__tagline { margin-top: 6px; font-size: 13px; color: var(--ink-grey); }
  .brand__tagline span { color: var(--ink-orange); }
  .sheet--front .brand { top: 40px; }
  .sheet--back .brand  { top: 58px; }

  /* orange field */
  .field {
    position: absolute; left: 0; width: 100%;
    background: linear-gradient(160deg, var(--orange-light) 0%, var(--orange) 50%, var(--orange-deep) 100%);
  }
  .sheet--front .field { top: 440px; height: 360px; }
  .sheet--back .field  { top: 170px; height: 630px; }

  /* photo placeholders */
  .photo { position: absolute; }
  .photo--consult {
    left: 0; top: 130px; width: 540px; height: 310px;
    background: linear-gradient(120deg, #c9b8a8 0%, #e8e6e2 45%, #b9c1c8 70%, #8f8a86 100%);
  }
  .photo-stack {
    position: absolute; left: 22px; top: 170px; width: 150px; height: 630px;
    display: flex; flex-direction: column;
  }
  .photo-stack .photo { position: static; flex: 1; }
  .photo--meeting { background: linear-gradient(135deg, #cfc7c0, #f0ece8 55%, #9a8d84); }
  .photo--desk    { background: linear-gradient(135deg, #dfe6ec, #9fb0bf 50%, #2c3036); }
  .photo--natal   { background: linear-gradient(135deg, #e9c7ad, #f4e3d6 50%, #9bc7c9); }
  .photo--produce { background: linear-gradient(135deg, #d9412b, #e88a34 40%, #9cb43a 70%, #e9c8d8); }

  /* front copy */
  .front-copy {
    position: absolute; left: 0; top: 480px; width: 100%;
    text-align: center; color: var(--white);
    font-size: 20px; line-height: 1.32;
  }
  .front-copy p + p { margin-top: 22px; }
  .front-copy strong { font-weight: 500; }
  .contact-band {
    position: absolute; left: 0; top: 690px; width: 100%; height: 64px;
    background: var(--band);
    display: flex; flex-direction: column; justify-content: center; align-items: center;
    color: var(--white); font-size: 16px; line-height: 1.35;
  }
  .contact-band .web { font-weight: 500; }

  /* service list */
  .services {
    position: absolute; left: 196px; top: 200px; width: 300px;
    list-style: none; color: var(--white);
    font-size: 16.5px; line-height: 1.3;
  }
  .services li + li { margin-top: 22px; }
  .services strong { font-weight: 500; }
</style>
</head>
<body>
<main class="spread">

  <section class="sheet sheet--front">
    <header class="brand">
      <div class="brand__name"><span class="brand__dot"></span>Quorvane Health</div>
      <p class="brand__tagline"><span>Connecting people.</span> Connecting care.</p>
    </header>

    <div class="photo photo--consult" role="img" aria-label="Photo of a smiling couple meeting a consultant at an office desk with a computer"></div>

    <div class="field"></div>

    <div class="front-copy">
      <p>Losing weight, diabetes care,<br>high cholestrol or switching to<br><strong>healthier lifestyle</strong> are now easy.</p>
      <p>Our consultants will assist you<br>to <strong>achieve</strong> it.</p>
    </div>

    <div class="contact-band">
      <span class="phone">1- (855).400.QUOR (7867)</span>
      <span class="web">www.Quorvane-health.com</span>
    </div>
  </section>

  <section class="sheet sheet--back">
    <header class="brand">
      <div class="brand__name"><span class="brand__dot"></span>Quorvane Health</div>
      <p class="brand__tagline"><span>Connecting people.</span> Connecting care.</p>
    </header>

    <div class="field"></div>

    <div class="photo-stack">
      <div class="photo photo--meeting" role="img" aria-label="Photo of a dietitian handing papers to a client across a desk"></div>
      <div class="photo photo--desk" role="img" aria-label="Photo of a computer monitor, keyboard, mouse and desk phone"></div>
      <div class="photo photo--natal" role="img" aria-label="Photo of two pregnant bellies"></div>
      <div class="photo photo--produce" role="img" aria-label="Photo of fresh fruit, vegetables and a yogurt drink"></div>
    </div>

    <ul class="services">
      <li><strong>Private one-on-one</strong> Nutrition counceling in the comfort of your home.</li>
      <li>Counceling provided by <strong>registered dietitians.</strong></li>
      <li>Nutrition counceling through <strong>HIPAA compliant video conferencing</strong>.</li>
      <li>Nutrition program and results overseen by <strong>primary care physicians</strong>.</li>
      <li><strong>Nutrition therapy</strong> to better handle diabetes, high Cholesterol, Triglycerides &amp; Blood Pressure.</li>
      <li><strong>Pre-Post Natal Nutrition</strong> &amp; Pediatric Nutrition.</li>
      <li><strong>Overcome barriers</strong> such as emotional or disordered eating.</li>
      <li>Provide <strong>meal-plans</strong> and help in creating grocery shopping list.</li>
    </ul>
  </section>

</main>
</body>
</html>
```